Business card for IT company

Looking for a business card for an IT company providing server, network, and application support to medium businesses. Company name is Calderwick Systems. Website is www.calderwicksystems.example, would like to use the green color that is on the homepage. Prefer design to be done in Illustrator. Please, only DESIGNERS apply - no PHP programmers attempting to do design. Thank you

Industry/Entity Type

Information Technology

Requirements
Must have
• Green
Should not have
• Template designs, or designs done by non-designer type people

```html
<!DOCTYPE html>
<html lang="en">
<head>
<meta charset="utf-8">
<title>Calderwick Systems – Business Card</title>
<link href="https://fonts.googleapis.com/css2?family=Roboto:wght@400;500;700&display=swap" rel="stylesheet">
<style>
  :root {
    --backdrop: #3b3b3b;
    --card-green: #76a534;
    --card-green-soft: #84b24a;
    --ink-light: #ffffff;
  }
  * { margin: 0; padding: 0; box-sizing: border-box; }
  html, body {
    width: 1105px;
    height: 1200px;
    overflow: hidden;
    background: var(--backdrop);
    font-family: "Roboto", Arial, sans-serif;
    color: var(--ink-light);
  }
  .card {
    position: absolute;
    left: 196px;
    width: 720px;
    height: 410px;
    border-radius: 22px;
    background: var(--card-green);
    overflow: hidden;
  }
  .card--front { top: 146px; }
  .card--back { top: 603px; }

  /* Front */
  .brand-mark {
    position: absolute;
    left: 521px;
    top: 41px;
    width: 116px;
    height: 116px;
    border-radius: 50%;
    background: var(--ink-light);
  }
  .brand-name {
    position: absolute;
    right: 40px;
    font-weight: 500;
    letter-spacing: 0.5px;
    white-space: nowrap;
  }
  .card--front .brand-name { top: 170px; font-size: 27px; }
  .location {
    position: absolute;
    left: 42px;
    top: 218px;
  }
  .location__place { font-size: 25px; font-weight: 700; line-height: 1.2; }
  .location__region { font-size: 18px; font-weight: 400; margin-top: 2px; }
  .divider {
    position: absolute;
    left: 42px;
    top: 285px;
    width: 638px;
    height: 2px;
    background: var(--ink-light);
  }
  .contacts {
    position: absolute;
    left: 42px;
    top: 297px;
    list-style: none;
    font-size: 18px;
  }
  .contacts li {
    display: flex;
    align-items: center;
    height: 28px;
  }
  .contacts svg { width: 18px; height: 18px; margin-right: 9px; fill: var(--ink-light); }

  /* Back */
  .watermark-circle {
    position: absolute;
    left: 15px;
    top: 11px;
    width: 386px;
    height: 386px;
    border-radius: 50%;
    background: var(--card-green-soft);
  }
  .card--back .brand-name { top: 290px; font-size: 32px; }
  .back-web {
    position: absolute;
    right: 42px;
    top: 340px;
    font-size: 18px;
  }
</style>
</head>
<body>
  <section class="card card--front" aria-label="Card front">
    <div class="brand-mark"></div>
    <div class="brand-name">Calderwick Systems</div>
    <div class="location">
      <div class="location__place">Harlow Ridge</div>
      <div class="location__region">Westvale County</div>
    </div>
    <div class="divider"></div>
    <ul class="contacts">
      <li>
        <svg viewBox="0 0 24 24" aria-hidden="true"><path d="M6.6 10.8c1.4 2.8 3.8 5.1 6.6 6.6l2.2-2.2c.3-.3.7-.4 1-.2 1.1.4 2.3.6 3.6.6.6 0 1 .4 1 1V20c0 .6-.4 1-1 1C10.6 21 3 13.4 3 4c0-.6.4-1 1-1h3.5c.6 0 1 .4 1 1 0 1.3.2 2.5.6 3.6.1.3 0 .7-.2 1L6.6 10.8z"/></svg>
        555.300.0144
      </li>
      <li>
        <svg viewBox="0 0 24 24" aria-hidden="true"><path d="M2 5h20v14H2V5zm2 2v.5l8 5 8-5V7H4zm0 2.8V17h16V9.8l-8 5-8-5z"/></svg>
        support@calderwicksystems.example
      </li>
      <li>
        <svg viewBox="0 0 24 24" aria-hidden="true"><path d="M12 2a10 10 0 1 0 0 20 10 10 0 0 0 0-20zm-1 17.9A8 8 0 0 1 4.2 10L9 14.8V16c0 1.1.9 2 2 2v1.9zm6.9-2.5c-.3-.8-1-1.4-1.9-1.4h-1v-3c0-.6-.4-1-1-1H8v-2h2c.6 0 1-.4 1-1V7h2c1.1 0 2-.9 2-2v-.4a8 8 0 0 1 2.9 12.8z"/></svg>
        www.calderwicksystems.example
      </li>
    </ul>
  </section>

  <section class="card card--back" aria-label="Card back">
    <div class="watermark-circle"></div>
    <div class="brand-name">Calderwick Systems</div>
    <div class="back-web">www.calderwicksystems.example</div>
  </section>
</body>
</html>
```